Medical Learning Web Design Project

The web site will be a site for medical students. It is aimed at providing a collaborative place for students to study, learn, question each other and challenge each other with learning. The site needs to have a section on the page that is for the content and this needs to be relatively clean and clinical. The surrounding elements will be informative (for the statistics, challenge etc). There will also be a slide-out screen that allows for the social/friend elements of the site.

The colour scheme needs to be clean and clinical where appropriate, but also engaging and exciting for the social/competitive elements.
Updates

Just for clarity: The site isn't expected to be 'coded' ... it is just the layered PSD files that I need.

Also, with regards to the navigation buttons ... they will never ALL be present at the same time so don't feel the need to design all on one page, but creativity around allowing few or many on a page will be an advantage ...

Thanks

Hi,

Please note that the image uploaded has been done as a wireframe by the developers. I am looking for a more creative and engaging way of presenting that content ...

Thanks

Hi all

Thank you all for the designs so far ...!

Please have a look at the new uploaded file, I am also looking not just for a 'templated home page' but also some different layouts that are represented in these wireframes. If the various layouts represented can be condensed down into 1 or 2 page templates with appropriate colour schemes to capture the type of content on the page (as already mentioned ... social .. competitive ... learning), then that will help me live the concepts better too! The friends tab for instance I have envisaged as a slider covering the screen and then sliding back when complete ... but let me see what creativity you can give to this ...!

Many thanks

Reason: Just allowing for final tweaks ...

Target Market(s)

Medical Students

Industry/Entity Type

Medical

Requirements
Must have
• - Not cluttered appearance
- Dynamic navigation (ie. site will be developed to only show relevant navigation buttons on each page ...)
- Navigation buttons (need to be individual buttons) will be: 'Home', 'Take the tour', 'What your peers say', 'Subscriptions', 'Free Signup', 'Contact us', 'Moderation', 'Statistics', 'Competition', 'Answer Questions', 'Post Questions', 'My profile', 'Friends'
- Please also ensure it is engaging for social elements and competitive elements (perhaps slightly different design for pages focussed on each element)
- Please also ensure that there is a masculine design and feminine design that has continuity for the site but depending on gender the design can be tailored to be more appealing (that means perhaps male social design, male competitive design, female social design, female competitive design ... without loosing continuity through the site).
- Photoshop PSD format
- Pixel perfect at least 1000 pixels wide (but the design needs to allow for various monitor sizes (only desktop or laptops ... not tablets or smart phones)

```html
<!DOCTYPE html>
<html lang="en">
<head>
<meta charset="utf-8">
<title>iMedora – The Medical Peer Review</title>
<link rel="stylesheet" href="https://fonts.googleapis.com/css2?family=Noto+Sans:wght@400;700&display=swap">
<style>
:root{
  --page:#ffffff;
  --head-bg:#f6f6f6;
  --sky:#b9dbe8;
  --olive:#9c9a12;
  --olive-dark:#747300;
  --nav-top:#93d6ea;
  --nav-bot:#4aa3b1;
  --teal:#5fb3c6;
  --ink:#1b1b1b;
  --muted:#555;
  --panel:#e4e4e4;
  --hero:#ebebeb;
  --news:#9fb6bd;
  --footer:#4e4646;
  --footer-active:#a6dcec;
  --link:#2f7fa0;
}
*{box-sizing:border-box;margin:0;padding:0}
html,body{width:1200px;height:981px;overflow:hidden}
body{position:relative;background:var(--page);font-family:"Noto Sans",sans-serif;color:var(--ink)}
.abs{position:absolute}

.masthead{left:0;top:0;width:1200px;height:185px;background:var(--head-bg)}
.sky-band{left:0;top:154px;width:1200px;height:31px;background:var(--sky)}
.brand-shape{left:0;top:0}
.brand-name{left:36px;top:38px;font-size:40px;font-weight:700;color:var(--olive);letter-spacing:-1px}
.brand-tag{left:39px;top:88px;font-size:15px;color:var(--ink)}

.rule{height:1px;background:#dcdcdc}
.quote{left:238px;top:52px;width:520px;text-align:center;font-size:13.5px;color:#333}
.quote-by{left:238px;top:78px;width:520px;text-align:center;padding-left:120px;font-size:11.5px;color:#333}
.stats-ask{left:238px;top:114px;width:520px;text-align:center;font-size:16px;color:#333}

.login{left:767px;top:53px;width:425px;height:84px;background:#fff;border-radius:6px}
.login label{position:absolute;font-size:10.5px;color:#111}
.login .field{position:absolute;top:40px;width:125px;height:21px;background:#e8f5fb;border:1px solid #b6dcea}
.login-btn{position:absolute;left:293px;top:36px;width:106px;height:29px;border-radius:4px;
  background:linear-gradient(#9ad9e9,#4aa3b1);font-size:15px;font-weight:700;color:#111;text-align:center;line-height:29px}
.login .small{position:absolute;top:67px;font-size:10.5px;color:var(--link)}
.keep-dot{display:inline-block;width:11px;height:11px;border-radius:50%;background:var(--teal);vertical-align:-1px;margin-right:6px}

.main-nav{left:31px;top:163px;width:1152px;height:50px;background:linear-gradient(var(--nav-top),var(--nav-bot))}
.main-nav a{position:absolute;top:0;height:50px;line-height:50px;text-align:center;font-size:14.5px;color:#111;text-decoration:none;border-right:1px solid rgba(255,255,255,.45)}
.main-nav a.active{background:var(--olive);color:#fff}

.search{left:31px;top:218px;width:721px;height:35px;background:#fff;border:1px solid #bfe2ee;border-radius:4px}

.hero{left:33px;top:257px;width:1150px;height:322px;background:var(--hero);border-radius:4px;overflow:hidden}
.hero-title{position:absolute;left:93px;top:56px;font-size:18px;font-weight:700;color:var(--olive-dark)}
.hero-list{position:absolute;left:122px;top:94px;list-style:none}
.hero-list li{font-size:15px;line-height:25px;color:#111;padding-left:18px;position:relative}
.hero-list li::before{content:"";position:absolute;left:0;top:10px;width:6px;height:6px;border-radius:50%;background:var(--teal)}
.hero-photo{position:absolute;left:650px;top:0;width:470px;height:322px;
  background:radial-gradient(ellipse at 45% 45%,#c9b7a6 0%,#dcd6d0 35%,#e6e6e6 70%,transparent 100%),
  linear-gradient(90deg,transparent,#d8dde4 40%,#b9c6dc 75%,transparent)}
.hero-arrow{position:absolute;top:138px}

.lower{left:35px;top:589px;width:1148px;height:278px;background:var(--panel)}
.box-title{position:absolute;background:#fafafa;border-radius:4px}
.works-title{left:70px;top:601px;width:397px;height:51px;font-size:18px;line-height:51px;text-align:center;padding-right:20px}
.video{left:94px;top:658px;width:346px;height:206px;background:#000}
.video-bar{position:absolute;left:0;bottom:0;width:346px;height:20px;background:linear-gradient(#f2f2f2,#c9c9c9)}
.news-title{left:474px;top:601px;width:397px;height:51px;padding:12px 15px;font-size:13px;line-height:15px}
.news{left:477px;top:655px;width:394px;height:207px;background:var(--news);border-radius:4px;padding:22px 16px;font-size:12px;line-height:18px}
.news p{margin-bottom:6px}
.news .date{margin:0 0 18px 4px}

.social{left:885px;top:601px;width:289px;height:259px;background:#fff;border:1px solid #cfcfcf}
.social .head{position:absolute;left:12px;top:12px}
.social .name{position:absolute;left:73px;top:12px;font-size:12px;font-weight:700;color:var(--link)}
.social .name span{font-weight:400;font-size:10px}
.like{position:absolute;left:73px;top:38px;width:50px;height:20px;border:1px solid #bbb;background:#eef1f7;font-size:10px;font-weight:700;text-align:center;line-height:18px;color:#333}
.like-note{position:absolute;left:133px;top:41px;font-size:10px;color:#333}
.count{position:absolute;left:12px;top:72px;width:262px;border-top:1px solid #ddd;padding-top:6px;font-size:10px;color:#333}
.people{position:absolute;left:12px;top:94px;display:grid;grid-template-columns:repeat(5,50px);column-gap:4px;row-gap:2px}
.person{font-size:9px;color:#666;text-align:center}
.person svg{display:block}
.plugin{position:absolute;left:12px;top:236px;width:262px;border-top:1px solid #ddd;padding-top:4px;font-size:9.5px;color:#444}
.plugin i{display:inline-block;width:12px;height:12px;background:#3b5b99;vertical-align:-2px;margin-right:4px}

.site-footer{left:36px;top:884px;width:1145px;height:82px;background:var(--footer)}
.site-footer a{position:absolute;top:22px;font-size:13.5px;color:#111;text-decoration:none}
.site-footer a.active{color:var(--footer-active)}
.copyright{position:absolute;left:0;top:58px;width:1145px;text-align:center;padding-right:30px;font-size:12px;color:#b0a8a8}
</style>
</head>
<body>

<header>
  <div class="abs masthead"></div>
  <div class="abs sky-band"></div>
  <svg class="abs brand-shape" width="260" height="186" viewBox="0 0 260 186" aria-hidden="true">
    <path d="M0 0 H213 C252 42 252 125 219 161 L219 186 H0 Z" fill="var(--sky)"/>
  </svg>
  <div class="abs brand-name">iMedora</div>
  <div class="abs brand-tag">The Medical Peer Review</div>

  <div class="abs rule" style="left:238px;top:43px;width:954px"></div>
  <p class="abs quote">"imedora keeps me ahaed of thr game constantly testing my knowledge..."</p>
  <p class="abs quote-by">Sam,doctor in training ,University of Northfield</p>
  <div class="abs rule" style="left:238px;top:105px;width:507px"></div>
  <p class="abs stats-ask">How will your stats compare?</p>

  <form class="abs login">
    <label style="left:25px;top:19px">Username</label>
    <label style="left:158px;top:19px">Password</label>
    <div class="field" style="left:24px"></div>
    <div class="field" style="left:156px"></div>
    <div class="login-btn">Login</div>
    <span class="small" style="left:25px"><span class="keep-dot"></span>keep Me Signed In</span>
    <span class="small" style="left:156px">Forgot your Password?</span>
  </form>

  <nav class="abs main-nav">
    <a style="left:115px;width:114px">Home</a>
    <a style="left:229px;width:147px">Take The Tour</a>
    <a class="active" style="left:376px;width:200px">What Your Peers Say</a>
    <a style="left:576px;width:161px">Subscriptio Plans</a>
    <a style="left:737px;width:136px">Free Signup</a>
    <a style="left:873px;width:132px;border-right:0">Contact Us</a>
  </nav>

  <div class="abs search"></div>
</header>

<section class="abs hero">
  <h1 class="hero-title">iMedora - The Medical Peer Review</h1>
  <ul class="hero-list">
    <li>Test your medical knowledge</li>
    <li>Answer a vast array of medical questions</li>
    <li>earn trophies as your knowledge increases</li>
    <li>rate questions from peers</li>
    <li>ask your own qustions</li>
    <li>Link to your friends and check their progress</li>
    <li>29.903 Questions answered!</li>
  </ul>
  <div class="hero-photo" role="img" aria-label="Photo of a smiling doctor in a white coat with a stethoscope, with two nurses in scrubs behind him"></div>
  <svg class="hero-arrow" style="left:22px" width="32" height="52" viewBox="0 0 32 52" aria-label="Previous slide" role="img">
    <path d="M28 2 L6 26 L28 50" fill="none" stroke="var(--teal)" stroke-width="8"/>
  </svg>
  <svg class="hero-arrow" style="left:1103px" width="32" height="52" viewBox="0 0 32 52" aria-label="Next slide" role="img">
    <path d="M4 2 L26 26 L4 50" fill="none" stroke="var(--teal)" stroke-width="8"/>
  </svg>
</section>

<main>
  <div class="abs lower"></div>

  <h2 class="abs box-title works-title" style="font-weight:400">How iMedora works</h2>
  <div class="abs video" role="img" aria-label="Introductory video player">
    <svg style="position:absolute;left:138px;top:55px" width="72" height="72" viewBox="0 0 72 72" aria-hidden="true">
      <circle cx="36" cy="36" r="34" fill="#6b6b6b" stroke="#9a9a9a" stroke-width="3"/>
      <path d="M28 22 L50 36 L28 50 Z" fill="#fff"/>
    </svg>
    <div class="video-bar">
      <svg width="346" height="20" viewBox="0 0 346 20" aria-hidden="true">
        <circle cx="10" cy="10" r="7" fill="#777"/>
        <path d="M8 6 L14 10 L8 14Z" fill="#fff"/>
        <rect x="26" y="9" width="170" height="2" fill="#4a8fc8"/>
        <circle cx="28" cy="10" r="3.5" fill="#3c7fc0"/>
        <text x="208" y="13" font-size="7" fill="#555">-0:00</text>
        <rect x="290" y="6" width="24" height="8" fill="#2f8ed6"/>
      </svg>
    </div>
  </div>

  <div class="abs box-title news-title">imedora Medical Peer Review<br><span style="font-size:14px">IMEDORA</span></div>
  <article class="abs news">
    <p>Lorem ipsum dolor sit amet, consectetuera iscing elit,Lorem ipsum dolor sit amet, consectetuera iscing elit,Lorem ipsum dolor sit amet, consectetuera iscing elit,</p>
    <p class="date">10/11/12</p>
    <p>Lorem ipsum dolor sit amet, consectetuera iscing elit,Lorem ipsum dolor sit amet, consectetuera iscing elit,Lorem ipsum dolor sit amet, consectetuera iscing elit,</p>
    <p class="date" style="margin-bottom:0">10/11/12</p>
  </article>

  <aside class="abs social">
    <svg class="head" width="50" height="50" viewBox="0 0 50 50" aria-hidden="true">
      <rect x=".5" y=".5" width="49" height="49" fill="#fff" stroke="#555"/>
      <path d="M0 0 L50 50 M50 0 L0 50" stroke="#555"/>
    </svg>
    <div class="name">iMedora <span>on Peerbook</span></div>
    <div class="like">Like</div>
    <div class="like-note">You like this.</div>
    <div class="count">22,407 people like <b>iMedora</b></div>
    <div class="people">
      <div class="person"><svg width="50" height="46" viewBox="0 0 50 46" aria-hidden="true"><rect x=".5" y=".5" width="49" height="45" fill="#fff" stroke="#555"/><path d="M0 0 L50 46 M50 0 L0 46" stroke="#555"/></svg>Person</div>
      <div class="person"><svg width="50" height="46" viewBox="0 0 50 46" aria-hidden="true"><rect x=".5" y=".5" width="49" height="45" fill="#fff" stroke="#555"/><path d="M0 0 L50 46 M50 0 L0 46" stroke="#555"/></svg>Person</div>
      <div class="person"><svg width="50" height="46" viewBox="0 0 50 46" aria-hidden="true"><rect x=".5" y=".5" width="49" height="45" fill="#fff" stroke="#555"/><path d="M0 0 L50 46 M50 0 L0 46" stroke="#555"/></svg>Person</div>
      <div class="person"><svg width="50" height="46" viewBox="0 0 50 46" aria-hidden="true"><rect x=".5" y=".5" width="49" height="45" fill="#fff" stroke="#555"/><path d="M0 0 L50 46 M50 0 L0 46" stroke="#555"/></svg>Person</div>
      <div class="person"><svg width="50" height="46" viewBox="0 0 50 46" aria-hidden="true"><rect x=".5" y=".5" width="49" height="45" fill="#fff" stroke="#555"/><path d="M0 0 L50 46 M50 0 L0 46" stroke="#555"/></svg>Person</div>
      <div class="person"><svg width="50" height="46" viewBox="0 0 50 46" aria-hidden="true"><rect x=".5" y=".5" width="49" height="45" fill="#fff" stroke="#555"/><path d="M0 0 L50 46 M50 0 L0 46" stroke="#555"/></svg>Person</div>
      <div class="person"><svg width="50" height="46" viewBox="0 0 50 46" aria-hidden="true"><rect x=".5" y=".5" width="49" height="45" fill="#fff" stroke="#555"/><path d="M0 0 L50 46 M50 0 L0 46" stroke="#555"/></svg>Person</div>
      <div class="person"><svg width="50" height="46" viewBox="0 0 50 46" aria-hidden="true"><rect x=".5" y=".5" width="49" height="45" fill="#fff" stroke="#555"/><path d="M0 0 L50 46 M50 0 L0 46" stroke="#555"/></svg>Person</div>
      <div class="person"><svg width="50" height="46" viewBox="0 0 50 46" aria-hidden="true"><rect x=".5" y=".5" width="49" height="45" fill="#fff" stroke="#555"/><path d="M0 0 L50 46 M50 0 L0 46" stroke="#555"/></svg>Person</div>
      <div class="person"><svg width="50" height="46" viewBox="0 0 50 46" aria-hidden="true"><rect x=".5" y=".5" width="49" height="45" fill="#fff" stroke="#555"/><path d="M0 0 L50 46 M50 0 L0 46" stroke="#555"/></svg>Person</div>
    </div>
    <div class="plugin"><i></i>Peerbook social plugin</div>
  </aside>
</main>

<footer class="abs site-footer">
  <a style="left:137px">Home</a>
  <a style="left:233px">Take The Tour</a>
  <a class="active" style="left:380px">What Your Peers Say</a>
  <a style="left:566px">Subscription Plans</a>
  <a style="left:731px">Free signup</a>
  <a style="left:850px">contact us</a>
  <a style="left:961px">sitemap</a>
  <p class="copyright">© 2012 imedora Limited</p>
</footer>

</body>
</html>
```